KMT Packaging design for beauty industry

Looking for my first product packaging design, tailored to reflect KMT’s branding and product benefits, along with mockup suggestions to bring it to life.

---

Front of the Box Copy
**Header**:
KMT Ionic Elite Stand-Up Dryer

**Subheader**:
Effortless Styling. Professional Results.

**Features (Use Icons + Text)**:
- **Adjustable Height**: Perfect for all users and settings.
- **Ionic Technology**: Faster drying, frizz-free results.
- **360° Heat Distribution**: Even styling every time.
- **Lightweight & Portable**: Easy to move and assemble.

**Call to Action (CTA)**:
*“Elevate Your Look with KMT Professional-Grade Tools.”*

---

### **Side Panel Copy**
**About KMT**:
"At KMT, we believe beauty is power. Our tools are designed with precision, ensuring every style feels as beautiful as you are."

**Key Benefits**:
- 3 Heat Settings for customizable control.
- Quiet operation for a professional salon experience.
- Compact foldable design for storage and travel.

**Contact Info**:
KMT Beauty | **www.KMTglowline.com**
Customer Care: care@KMTglowline.com

---

### **Back Panel Copy**
**Product Specifications**:
- Voltage: 110V-240V
- Adjustable Height Range: X to Y inches
- Dryer Weight: X lbs

**What’s Included**:
- 1 Stand-Up Dryer
- Adjustable Stand
- User Manual

**Care Instructions**:
"Clean with a damp cloth after use. Store in a cool, dry place."

**Certifications**:
(Include icons for QX, CE, RoHS, and recycling).

**Barcode Area**: Leave space for the UPC code.

---

### **Mockup Suggestions**
1. **Front View**:
- Use a glossy royal purple background with a clean, central placement of the KMT logo in metallic gold.
- Include a product photo or 3D render in high resolution showing the dryer in action or as a standalone image.
- Highlight features using icons with gold or white text.

2. **Side View**:
- Use a lifestyle image (e.g., a stylist using the dryer in a salon).
- Incorporate a vertical gold stripe or gradient to add luxury while separating text sections.

3. **Back View**:
- A clean layout with product details, specifications, and what's included.
- Use gold accents to frame sections for easy readability.

4. **Top Panel**:
- Simple branding with just the KMT logo and tagline: *"Keep Making Trends."*

The competition:
https://www.velmorashop.com/products/swift-blaze-07142?ref=QzT4pLm8Wn2Rv6Xc

Feel free to use the phots by the "the completion" but remove logo and add KMT logo .
https://files.pondercloud.com/folders/7gRt2KqWz9LmXv4NbPa?share=link
Size: 48x36.5x48 CM

Logo: https://files.pondercloud.com/folders/7gRt2KqWz9LmXv4NbPa?share=link
Also im not able to attached the AI file of the logo. Please message me your email and I'll email it to you.

Thank you!
Happy designing!

Target Market(s)

Target Audience for KMT’s First Product Demographics: Age: 18-40 years old Gender: Primarily women Income Level: Middle to upper-middle income, willing to invest in quality beauty products. Geographics: Urban and suburban areas across the U.S., where beauty culture is strong and highly influenced by social media and fashion trends. Psychographics: Beauty Enthusiasts: Individuals who prioritize their appearance and enjoy experimenting with beauty products. Trendsetters: Consumers who follow the latest beauty trends, influenced by social media and influencers. Self-Expression Advocates: Those who see beauty as a form of self-care and a way to express their personality and confidence. Behavioral Characteristics: Purchase Habits: Frequently buy beauty tools and products online or in beauty supply stores. Look for high-quality, professional-grade, and aesthetically pleasing products. Product Expectations: Easy-to-use, reliable, and results-driven. Luxurious feel without an excessively high price point. Engagement: Active on social media platforms like Pictavia, ZapReel, and ViewLoom. Trust peer reviews, influencer recommendations, and user-generated content. Customer Needs: Products that simplify beauty routines. Tools and supplies that are versatile and cater to diverse beauty needs, particularly for African American women (a key segment for KMT).

Industry/Entity Type

Industry Overview Primary Industry: Beauty and Personal Care: Encompasses products and tools for hair, skin, nails, and cosmetics. Sub-Sector: Hair Care & Styling Tools: Includes professional-grade tools like dryers, flat irons, and curling wands, along with supporting products like shampoos, conditioners, and styling creams.

Font styles to use
Serif

Requirements
Must have
• Must-Haves for the Packaging Brand Identity: Prominent display of the KMT logo in metallic gold to reinforce brand recognition. Consistent use of royal purple as the background color with metallic gold and white typography for a luxurious feel. Clear Product Information: Product Name: Clearly labeled as "KMT Ionic Elite Stand-Up Dryer" on the front. Key Features: Use icons with text to highlight: Adjustable Height Ionic Technology 360° Heat Distribution Lightweight & Portable Visual Appeal: High-quality product image or 3D render showcasing the dryer. Lifestyle imagery on the side panels to show the product in use, emphasizing its professional and stylish appeal. Call to Action (CTA): Include a tagline like: “Elevate Your Look with KMT Professional-Grade Tools.” Functional Details: Product Specifications: Include voltage, dimensions, and weight on the back panel. What’s Included: Clearly list all box contents. Certifications and Compliance: Add icons for QX, CE, RoHS, and recycling to ensure credibility and eco-conscious appeal. Contact Information: Website: www.KMTglowline.com Customer care email: care@KMTglowline.com Barcode Area: Leave space for the UPC code on the back panel. Packaging Consistency: Uniform design elements across all panels for a cohesive look (color scheme, typography, and layout). Professional and Luxurious Finish: A glossy or matte finish with possible embossing on the logo for a premium touch.
Nice to have
• Nice-to-Have Elements Interactive Design Features: QR Code: Link to a demo video, tutorial, or assembly instructions for added customer engagement. Augmented Reality (AR): An AR feature that allows customers to see the dryer in a 360° view or visualize it in their space. Texture and Finishes: Embossed or Debossed Details: Highlight the KMT logo or key features with embossed or debossed effects for a tactile, premium feel. Spot UV Coating: Add gloss to key areas like the logo or icons to make them pop. Eco-Friendly Touch: Recyclable or biodegradable materials for the packaging. A small section emphasizing sustainability with a message like: “KMT is committed to beauty and the environment.” Unique Structural Design: Magnetic flap or window cutout to allow customers to peek at the product inside. A handle or carrying feature for easy transport, aligning with the portable nature of the dryer. Inspirational Touch: Include a short, empowering quote or message on the inside flap, such as: “Every style tells a story—KMT helps you write yours.” Custom Illustrations: Subtle, artistic illustrations (e.g., flowing hair, heat waves) integrated into the design background to emphasize beauty and technology. Additional Branding Elements: A tagline or hashtag like #KMTRadiance to encourage customers to share their experience on social media. Icons or badges for unique selling points, such as "Professional-Grade Quality" or "Salon Approved." Convenience Features: Printed assembly instructions or key features inside the box for ease of use. Perforated areas for easy opening. Color Gradients or Patterns: Add subtle gradients in the royal purple background for depth. Incorporate gold patterns (like geometric shapes or soft waves) for a modern touch. Seasonal or Limited-Edition Elements: A special ribbon or sticker indicating a “First Edition” or “Limited Release” to create exclusivity.
Should not have
• What the Packaging Should NOT Have Overcrowded Design: Avoid cluttering the box with too much text, small icons, or excessive design elements. A clean and elegant layout is key. Low-Quality Imagery: Do not use low-resolution product photos or stock images that don’t align with the premium look of your brand. Overused or Generic Icons: Skip overly common or generic symbols (e.g., basic checkmarks or lightning bolts). Custom, elegant icons are more appealing. Inconsistent Branding: Do not use colors, fonts, or design elements that stray from the royal purple, gold, and white branding. Consistency builds recognition. Unclear Information: Avoid vague or ambiguous descriptions. Clearly explain features, benefits, and product specifications. Cheap Materials: Packaging that feels flimsy or poorly constructed can reduce perceived value. Invest in durable materials. Overly Trendy Fonts: Avoid overly decorative or hard-to-read fonts. Stick with modern, clean typography that aligns with luxury branding. Busy Backgrounds: Don’t use loud patterns, excessive gradients, or background images that distract from key elements like the logo and product image. Misleading Claims: Avoid exaggerated or false claims (e.g., “World’s Best Dryer”) that could harm your brand’s credibility. Unnecessary Jargon: Avoid overly technical language that might confuse customers. Use simple, benefit-driven terms instead. Cliché Beauty Imagery: Skip generic, overused beauty symbols (e.g., oversized hair strands or glowing light effects) that don’t add value or originality. Lack of Contrast: Ensure text is easily readable. Avoid color combinations (like gold on light backgrounds) that reduce legibility. Lack of Accessibility: Don’t forget about inclusive design. Avoid small text or icons that are hard to read for visually impaired customers.

```html
<!DOCTYPE html>
<html lang="en">
<head>
<meta charset="utf-8">
<title>KMT Ionic Elite Stand-Up Dryer – Packaging Panels</title>
<link href="https://fonts.googleapis.com/css2?family=Poppins:wght@400;500;600;700&family=Montserrat:wght@700;800&family=Roboto+Condensed:wght@400;700&display=swap" rel="stylesheet">
<style>
  :root{
    --stage:#e6e6e8;
    --purple-top:#5a3591;
    --purple-mid:#3a2266;
    --ink:#17141c;
    --ink-soft:#221c2b;
    --gold:#c9a24a;
    --gold-light:#f0cf6a;
    --gold-deep:#8f6a25;
    --white:#ffffff;
    --band:#4a3180;
  }
  *{box-sizing:border-box;margin:0;padding:0}
  html,body{width:1200px;height:900px;overflow:hidden;background:var(--stage)}
  body{font-family:"Poppins",sans-serif;color:var(--white);position:relative}

  .panel{
    position:absolute;top:240px;height:420px;overflow:hidden;
    background:linear-gradient(180deg,var(--purple-top) 0%,var(--purple-mid) 40%,var(--ink-soft) 72%,var(--ink) 100%);
    box-shadow:0 18px 40px rgba(0,0,0,.18);
  }
  .panel--side{left:40px;width:310px}
  .panel--front{left:350px;width:390px;border-left:1px solid rgba(0,0,0,.35)}
  .panel--back{left:770px;width:390px}

  .gold-rule{position:absolute;left:0;right:0;height:3px;
    background:linear-gradient(90deg,var(--gold-deep),var(--gold-light),var(--gold-deep))}

  .brand{color:var(--gold);font-family:"Poppins",sans-serif;font-weight:600;text-align:center;line-height:1}
  .brand__name{display:block;font-size:60px;letter-spacing:2px}
  .brand__tag{display:block;font-size:9.5px;letter-spacing:2.5px;margin-top:8px}

  /* side */
  .about{position:absolute;top:40px;left:24px;right:24px;font-family:"Roboto Condensed",sans-serif;font-size:10.5px;line-height:1.35;text-align:center}
  .benefits{position:absolute;top:100px;left:34px;right:20px;list-style:none;font-family:"Roboto Condensed",sans-serif;font-size:10.5px}
  .benefits li{margin-bottom:10px;padding-left:8px;position:relative}
  .benefits li::before{content:"";position:absolute;left:0;top:5px;width:4px;height:4px;border-radius:50%;background:var(--gold-light)}
  .lifestyle{position:absolute;left:0;right:0;top:200px;height:160px;
    background:linear-gradient(90deg,#2a2430 0%,#4a3b3a 30%,#2b2233 60%,#1f1a24 100%)}
  .side-foot{position:absolute;left:0;right:0;bottom:0;height:58px;background:var(--ink)}
  .side-foot .gold-rule{top:0}
  .side-brand{position:absolute;left:16px;top:16px;color:var(--gold);font-weight:600;font-size:24px;line-height:1}
  .side-brand small{font-size:8px;letter-spacing:2px;margin-left:6px;vertical-align:middle}
  .contact{position:absolute;right:14px;top:20px;font-family:"Roboto Condensed",sans-serif;font-size:9px;text-align:right;line-height:1.4}
  .contact b{font-weight:700}

  /* front */
  .panel--front .brand{position:absolute;top:36px;left:28px;width:170px}
  .cta{position:absolute;top:170px;left:28px;font-family:"Roboto Condensed",sans-serif;font-size:12px;color:var(--gold-light);line-height:1.5}
  .cta mark{display:inline-block;background:linear-gradient(90deg,var(--gold-light),var(--gold));color:var(--ink);padding:0 5px}
  .product{position:absolute;right:10px;top:20px;width:150px;height:320px;border-radius:70px 70px 10px 10px;
    background:linear-gradient(180deg,#2b2b2f 0%,#5a5a60 45%,#1b1b1e 100%)}
  .title{position:absolute;left:26px;top:252px;font-family:"Montserrat",sans-serif;font-weight:800;font-size:25px;line-height:1.05;color:var(--gold)}
  .title span{display:block;color:var(--gold-light)}
  .subhead{position:absolute;left:26px;top:312px;background:var(--band);font-family:"Montserrat",sans-serif;font-weight:700;font-size:9.5px;padding:4px 8px;letter-spacing:.3px}
  .front-foot{position:absolute;left:0;right:0;bottom:0;height:64px;background:var(--ink)}
  .front-foot .gold-rule{top:0}
  .features{position:absolute;left:12px;right:8px;top:14px;display:flex;gap:6px;list-style:none}
  .feature{flex:1;display:flex;gap:4px;align-items:flex-start;font-family:"Roboto Condensed",sans-serif;font-size:7.5px;line-height:1.25}
  .feature b{display:block;font-weight:700}
  .feature svg{flex:none}

  /* back */
  .panel--back .brand{position:absolute;top:30px;left:18px;width:115px}
  .panel--back .brand__name{font-size:50px;letter-spacing:1px}
  .panel--back .brand__tag{font-size:7px;letter-spacing:1.6px;margin-top:7px}
  .spec-title{position:absolute;top:28px;left:176px;font-family:"Poppins",sans-serif;font-weight:700;font-size:14px;color:var(--gold);letter-spacing:.5px;white-space:nowrap}
  .drawing{position:absolute;left:180px;top:64px;width:80px;height:272px;border-radius:38px 38px 6px 6px;
    background:linear-gradient(180deg,rgba(255,255,255,.12),rgba(255,255,255,.03))}
  .guides{position:absolute;left:0;top:0}
  .callout{position:absolute;font-size:8.5px;line-height:1.15;white-space:nowrap}
  .callout b{font-weight:700}
  .callout--height{left:36px;top:165px;width:66px;text-align:center}
  .callout--voltage{left:285px;top:148px}
  .callout--weight{left:266px;top:226px}
  .care{position:absolute;left:30px;top:228px;width:110px;font-size:8.5px;line-height:1.28}
  .care b{font-weight:700;display:block}
  .included{position:absolute;left:24px;top:292px;width:92px;padding:5px 7px;border-radius:3px;
    background:linear-gradient(90deg,var(--gold-light),var(--gold-deep));color:var(--ink);font-size:8px;line-height:1.2}
  .included b{font-weight:700;display:block}
  .back-foot{position:absolute;left:0;right:0;bottom:0;height:58px;background:var(--ink)}
  .back-foot .gold-rule{top:0}
  .certs{position:absolute;left:30px;top:18px;display:flex;gap:7px;align-items:center}
  .barcode-space{position:absolute;right:30px;top:13px;width:66px;height:30px;background:var(--white);
    color:var(--ink);font-family:"Poppins",sans-serif;font-weight:600;font-size:7px;display:flex;align-items:center;justify-content:center}
</style>
</head>
<body>

<section class="panel panel--side" aria-label="Side panel">
  <p class="about">At KMT, we believe beauty is power. Our tools are designed with precision, ensuring every style feels as beautiful as you are.</p>
  <ul class="benefits">
    <li>3 Heat Settings for customizable control.</li>
    <li>Quiet operation for a professional salon experience.</li>
    <li>Compact foldable design for storage and travel.</li>
  </ul>
  <div class="lifestyle" role="img" aria-label="Lifestyle photo of a woman beside the stand-up hood dryer in a softly lit room"></div>
  <footer class="side-foot">
    <div class="gold-rule"></div>
    <div class="side-brand">KMT<small>KEEP MAKING TRENDS</small></div>
    <div class="contact">www.<b>KMTglowline</b>.com<br>Customer Care: <b>care@KMTglowline.com</b></div>
  </footer>
</section>

<section class="panel panel--front" aria-label="Front panel">
  <div class="brand"><span class="brand__name">KMT</span><span class="brand__tag">KEEP MAKING TRENDS</span></div>
  <p class="cta">Elevate Your Look with KMT<br><mark>Professional-Grade Tools.</mark></p>
  <div class="product" role="img" aria-label="Product render of the black stand-up hood dryer with clear visor on a pole"></div>
  <h1 class="title"><span>KMT IONIC ELITE</span>STAND-UP DRYER</h1>
  <p class="subhead">EFFORTLESS STYLING. PROFESSIONAL RESULTS</p>
  <footer class="front-foot">
    <div class="gold-rule"></div>
    <ul class="features">
      <li class="feature">
        <svg width="18" height="18" viewBox="0 0 18 18"><rect x="1" y="1" width="16" height="16" rx="2" fill="#c9a24a"/><path d="M9 4v10M6 6.5 9 4l3 2.5M6 11.5 9 14l3-2.5" stroke="#17141c" stroke-width="1.4" fill="none"/></svg>
        <span><b>Adjustable Height:</b>Perfect for all users and settings.</span>
      </li>
      <li class="feature">
        <svg width="18" height="18" viewBox="0 0 18 18" fill="none" stroke="#c9a24a" stroke-width="1.2"><circle cx="9" cy="9" r="7.5"/><circle cx="9" cy="9" r="2"/><ellipse cx="9" cy="9" rx="6" ry="2.5"/></svg>
        <span><b>Ionic Technology:</b>Faster drying, frizz-free results.</span>
      </li>
      <li class="feature">
        <svg width="18" height="18" viewBox="0 0 18 18" fill="none" stroke="#c9a24a" stroke-width="1.4"><path d="M15 9a6 6 0 1 1-2-4.5"/><path d="M13.5 2v3h-3"/></svg>
        <span><b>360° Heat Distribution:</b>Even styling every time.</span>
      </li>
      <li class="feature">
        <svg width="18" height="18" viewBox="0 0 18 18" fill="none" stroke="#c9a24a" stroke-width="1.4"><path d="M9 2v14M5.5 5.5 9 2l3.5 3.5M5.5 12.5 9 16l3.5-3.5"/></svg>
        <span><b>Adjustable Height:</b>Perfect for all users and settings.</span>
      </li>
    </ul>
  </footer>
</section>

<section class="panel panel--back" aria-label="Back panel">
  <div class="brand"><span class="brand__name">KMT</span><span class="brand__tag">KEEP MAKING TRENDS</span></div>
  <h2 class="spec-title">SPECIFICATIONS</h2>
  <div class="drawing" role="img" aria-label="Line drawing of the hood dryer on a five-wheel adjustable stand"></div>
  <svg class="guides" width="390" height="420" viewBox="0 0 390 420" fill="none" stroke="#ffffff" stroke-width="1.3" aria-hidden="true">
    <path d="M165 82H148V342H165"/>
    <path d="M148 175H110"/>
    <rect x="105" y="172.5" width="5" height="5"/>
    <path d="M262 70H314V136"/>
    <rect x="311.5" y="136" width="5" height="5"/>
    <path d="M240 231H256"/>
    <rect x="256" y="228.5" width="5" height="5"/>
  </svg>
  <p class="callout callout--height"><b>ADJUSTABLE<br>HEIGHT RANGE:</b><br>X to Y inches</p>
  <p class="callout callout--voltage"><b>VOLTAGE</b><br>110V–240V</p>
  <p class="callout callout--weight"><b>DRYER WEIGHT:</b> X lbs</p>
  <p class="care"><b>CARE INSTRUCTIONS:</b>Clean with a damp cloth after use. Store in a cool, dry place.</p>
  <div class="included"><b>INCLUDED:</b>1 Stand-Up Dryer<br>Adjustable Stand<br>User Manual</div>
  <footer class="back-foot">
    <div class="gold-rule"></div>
    <div class="certs" aria-label="Certification marks">
      <svg width="20" height="20" viewBox="0 0 20 20"><rect x="2" y="2" width="16" height="16" rx="3" fill="none" stroke="#fff" stroke-width="2"/></svg>
      <svg width="20" height="20" viewBox="0 0 20 20"><circle cx="10" cy="10" r="8" fill="#fff"/></svg>
      <svg width="20" height="20" viewBox="0 0 20 20"><circle cx="10" cy="10" r="8" fill="none" stroke="#fff" stroke-width="2"/><path d="M6 10.5l3 3 5-6" fill="none" stroke="#fff" stroke-width="2"/></svg>
      <svg width="20" height="20" viewBox="0 0 20 20"><circle cx="10" cy="10" r="8" fill="none" stroke="#fff" stroke-width="2"/><circle cx="10" cy="10" r="4" fill="#fff"/></svg>
    </div>
    <div class="barcode-space">BARCODE</div>
  </footer>
</section>

</body>
</html>
```